Pediatric Dentist Business Card

I need a business card designed for a dentist who works exclusively with children.
We prefer designs that are out of ordiary that is fun and interesting to kids.

there is no logo since this is a dentists office. The name of the doctor is "Tavor Kesh" if you want to get creative with that.

Target Market(s)

Kids

Industry/Entity Type

Business

Contact Information for Business Card

Anythings that is creative

Colors

Designer to choose colors to be used in the design.

```html
<!DOCTYPE html>
<html lang="en">
<head>
<meta charset="utf-8">
<title>Tavor Kesh – Business Card</title>
<link href="https://fonts.googleapis.com/css2?family=Questrial&display=swap" rel="stylesheet">
<style>
  :root {
    --backdrop: #636363;
    --card: #ffffff;
    --band-top: #f9ac40;
    --band-bottom: #ee4f06;
    --edge: #6b2a10;
    --ink: #231f20;
    --sun: #ffc60b;
    --brand: #f05a0a;
    --accent: #f9a13a;
  }
  html, body {
    margin: 0;
    padding: 0;
    width: 1185px;
    height: 1200px;
    overflow: hidden;
    background: var(--backdrop);
    font-family: "Questrial", "Century Gothic", sans-serif;
  }
  .card {
    position: absolute;
    left: 248px;
    width: 690px;
    height: 388px;
    background: var(--card);
    overflow: hidden;
  }
  .card--front { top: 190px; }
  .card--back { top: 622px; }
  .card--front::after {
    content: "";
    position: absolute;
    left: 0;
    right: 0;
    bottom: 0;
    height: 2px;
    background: var(--edge);
  }
  .card__band {
    position: absolute;
    inset: 0;
    width: 100%;
    height: 100%;
  }
  .brand {
    position: absolute;
    display: flex;
    align-items: center;
    gap: 10px;
    font-size: 26px;
    color: var(--brand);
    white-space: nowrap;
  }
  .brand__dot {
    width: 22px;
    height: 22px;
    border-radius: 50%;
    background: var(--sun);
  }
  .card--front .brand {
    left: 467px;
    top: 146px;
    transform: translateX(-50%);
  }
  .brand--faint {
    left: 36px;
    top: 300px;
    font-size: 28px;
    color: var(--sun);
  }
  .holder-name {
    position: absolute;
    left: 355px;
    top: 46px;
    margin: 0;
    font-size: 46px;
    font-weight: 400;
    color: var(--ink);
    letter-spacing: 0.5px;
    white-space: nowrap;
  }
  .contact {
    position: absolute;
    left: 463px;
    top: 137px;
    margin: 0;
    padding: 0;
    list-style: none;
    font-size: 14px;
    color: var(--ink);
  }
  .contact__item {
    display: flex;
    align-items: center;
    height: 24px;
  }
  .contact__item--address { margin-top: 8px; }
  .contact__icon {
    width: 16px;
    height: 16px;
    margin-right: 14px;
    fill: var(--accent);
  }
</style>
</head>
<body>

<section class="card card--front">
  <svg class="card__band" viewBox="0 0 540 304" preserveAspectRatio="none" role="img" aria-label="Soft orange wave band decoration">
    <defs>
      <linearGradient id="bandFront" x1="0" y1="0" x2="0" y2="1">
        <stop offset="0" stop-color="var(--band-top)"/>
        <stop offset="1" stop-color="var(--band-bottom)"/>
      </linearGradient>
    </defs>
    <path fill="url(#bandFront)" d="M0,68 C140,160 280,256 410,258 C480,259 520,215 540,188 L540,304 L0,304 Z"/>
  </svg>
  <div class="brand"><span class="brand__dot"></span>Kesh Kids Dental</div>
</section>

<section class="card card--back">
  <svg class="card__band" viewBox="0 0 540 304" preserveAspectRatio="none" role="img" aria-label="Soft orange wave band decoration">
    <defs>
      <linearGradient id="bandBack" x1="0" y1="0" x2="0" y2="1">
        <stop offset="0" stop-color="var(--band-top)"/>
        <stop offset="1" stop-color="var(--band-bottom)"/>
      </linearGradient>
    </defs>
    <path fill="url(#bandBack)" d="M0,68 C140,160 280,256 410,258 C480,259 520,215 540,188 L540,304 L0,304 Z"/>
  </svg>
  <div class="brand brand--faint">Kesh Kids Dental</div>

  <h1 class="holder-name">Tavor Kesh</h1>
  <ul class="contact">
    <li class="contact__item">
      <svg class="contact__icon" viewBox="0 0 16 16"><path d="M3.5 1.5 L6 4 L4.6 6 C5.6 8.2 7.8 10.4 10 11.4 L12 10 L14.5 12.5 L12.6 14.6 C7 14 2 9 1.4 3.4 Z"/></svg>
      000 0000 000
    </li>
    <li class="contact__item">
      <svg class="contact__icon" viewBox="0 0 16 16"><path d="M1 3.5 H15 V12.5 H1 Z M2 4.5 L8 9 L14 4.5" stroke="#fff" stroke-width="1"/></svg>
      smile@keshkids.com
    </li>
    <li class="contact__item contact__item--address">
      <svg class="contact__icon" viewBox="0 0 16 16"><path d="M8 1.5 L15 8 H13 V14.5 H9.5 V10.5 H6.5 V14.5 H3 V8 H1 Z"/></svg>
      12 Elm Row
    </li>
  </ul>
</section>

</body>
</html>
```